Geschäftspapiere für Rechtsanwaltskanzlei
Zielgruppe
Rechtsanwaltskanzlei bestehend aus 2 Anwälten u.a. mit bau-, miet- und familienrechtlichem Tätigkeitsschwerpunkt
Es werden hauptsächlich Verbraucher und mittelständische Unternehmen angesprochen; Zielgruppe sind auch Wohnungsbauunternehmen und Immobiliengesellschaften
Aufgabenstellung
Es wird ein hochwertiges, klares, nicht verspieltes Design gesucht, dass Durchsetzungskraft vermittelt
Kanzleiinhaber ist Stefan Brüning, Rechtsanwältin Helga Lindner scheidet zum 31.12.2019 aus. Das Ausscheidungsdatum muss auf den Briefkopf aufgenommen werden.
Die Bögen werden erst ab dem 01.01.2020 verwendet.
Die wesentlichen Kenndaten können von dem Briefbogen übernommen werden.
weitere Informationen finden sich auf der Homepage ra-bruening-beispiel.de
Das Logo selbst sowie Unterüberschriften sollen in UV-Lack gedruckt werden
Weitere Designideen angelehnt an baurechtliche Themen habe ich angefügt

```html
<!DOCTYPE html>
<html lang="de">
<head>
<meta charset="utf-8">
<title>Briefbogen Brüning &amp; Lindner Rechtsanwälte</title>
<link href="https://fonts.googleapis.com/css2?family=Open+Sans:wght@400;600;700&display=swap" rel="stylesheet">
<style>
  :root {
    --red: #d6001c;
    --black: #1d1d1b;
    --ink: #2b2b2b;
    --paper: #ffffff;
    --backdrop: #e6e7e8;
    --rule: #6a6a6a;
  }
  * { box-sizing: border-box; margin: 0; padding: 0; }
  html, body { width: 1200px; height: 1010px; overflow: hidden; }
  body {
    background: var(--backdrop);
    font-family: "Open Sans", Arial, sans-serif;
    color: var(--ink);
    position: relative;
  }
  .letterhead {
    position: absolute;
    left: 260px; top: 24px;
    width: 680px; height: 962px;
    background: var(--paper);
    box-shadow: 0 6px 24px rgba(0,0,0,.12);
    overflow: hidden;
  }
  .brand {
    position: absolute;
    left: 420px; top: 54px;
    width: 230px;
  }
  .brand-name {
    display: flex; align-items: center; gap: 8px;
    font-weight: 700; font-size: 18px; color: var(--red);
    letter-spacing: .2px; text-transform: uppercase;
    white-space: nowrap;
  }
  .brand-mark { width: 13px; height: 13px; background: var(--black); flex: none; }
  .brand-sub {
    font-weight: 600; font-size: 10.5px; letter-spacing: 5.5px;
    text-transform: uppercase; color: var(--black);
    margin: 3px 0 0 21px;
  }
  .sender-line {
    position: absolute; left: 62px; top: 212px;
    font-size: 7.5px; color: var(--ink);
    border-bottom: .8px solid var(--ink); padding-bottom: 1px;
  }
  .sender-line .sep { color: var(--red); margin: 0 3px; }
  .fold-mark { position: absolute; left: 22px; top: 330px; width: 10px; border-top: .8px solid var(--rule); }
  .sidebar {
    position: absolute; left: 470px; top: 128px;
    width: 200px; height: 650px;
    border-left: .8px solid var(--rule);
    padding-left: 12px;
    font-size: 8.6px; line-height: 1.3;
  }
  .sidebar section { margin-bottom: 11px; }
  .sidebar h3 { color: var(--red); font-size: 8.8px; font-weight: 700; }
  .sidebar .role { font-weight: 700; color: var(--black); }
  .sidebar .note { font-size: 6.8px; }
  .badge {
    width: 56px; height: 24px; border-radius: 3px;
    background: linear-gradient(90deg, var(--red), #9a9a9a);
    margin: 4px 0 14px;
  }
  .firm { font-weight: 700; font-size: 10px; text-transform: uppercase; color: var(--black); line-height: 1.15; margin-bottom: 9px; }
  .contact-row { display: flex; align-items: center; gap: 5px; white-space: nowrap; }
  .contact-row svg { width: 8px; height: 8px; flex: none; }
  .footer { position: absolute; left: 0; bottom: 0; width: 680px; height: 200px; }
  .footer svg { position: absolute; inset: 0; }
  .bank {
    position: absolute; left: 30px; bottom: 22px;
    color: #fff; font-size: 8.8px; white-space: nowrap;
  }
  .bank .dot { color: var(--red); margin: 0 7px; }
  .web {
    position: absolute; right: 26px; bottom: 106px;
    color: #fff; font-size: 9px; display: flex; align-items: center; gap: 5px;
    white-space: nowrap;
  }
  .web .dot { width: 7px; height: 7px; border-radius: 50%; background: var(--red); }
</style>
</head>
<body>
<main class="letterhead">
  <header class="brand">
    <div class="brand-name"><span class="brand-mark"></span>Brüning &amp; Lindner</div>
    <div class="brand-sub">Rechtsanwälte</div>
  </header>

  <p class="sender-line">BRÜNING &amp; LINDNER<span class="sep">|</span>Rechtsanwälte<span class="sep">|</span>Lindenweg 12<span class="sep">|</span>66111 Musterstadt</p>
  <span class="fold-mark"></span>

  <aside class="sidebar">
    <section>
      <h3>Stefan Brüning</h3>
      <p class="role">Rechtsanwalt</p>
    </section>
    <section>
      <h3>Tätigkeitsschwerpunkte:</h3>
      <p>Immobilienrecht<br>Bau- und Werkvertragsrecht<br>Miet- und WEG-Recht</p>
    </section>
    <section>
      <h3>Interessenschwerpunkte:</h3>
      <p>Arbeitsrecht<br>Widerruf von Verbraucherdarlehen<br>Sozialversicherungsrecht</p>
    </section>
    <section>
      <h3>Helga Lindner</h3>
      <p class="role">Rechtsanwältin</p>
      <p class="note">(bis 31.12.2019)</p>
    </section>
    <section>
      <h3>Tätigkeitsschwerpunkte:</h3>
      <p>Familienrecht<br>Erbrecht<br>Allgemeines Zivilrecht<br>Straßenverkehrsrecht</p>
    </section>
    <div class="badge" role="img" aria-label="Mitgliedschaftsabzeichen"></div>
    <p class="firm">Brüning &amp; Lindner<br>Rechtsanwälte</p>
    <section>
      <h3>Anschrift:</h3>
      <p>Lindenweg 12<br>66111 Musterstadt</p>
    </section>
    <section>
      <h3>Kontakt:</h3>
      <p class="contact-row"><svg viewBox="0 0 10 10"><path d="M2 1l2 2-1 1.5c.8 1.3 1.7 2.2 3 3L7.5 6.5l2 2-1.5 1.5C4.5 9.5.5 5.5 0 2z" fill="var(--red)"/></svg>0681 / 1234560</p>
      <p class="contact-row"><svg viewBox="0 0 10 10"><rect x="1" y="3" width="8" height="5" rx="1" fill="var(--red)"/><rect x="3" y="1" width="4" height="2" fill="var(--red)"/></svg>0681 / 12345617</p>
    </section>
    <section>
      <h3>Email:</h3>
      <p class="contact-row"><svg viewBox="0 0 10 10"><rect x="0" y="2" width="10" height="6" fill="var(--red)"/><path d="M0 2l5 3.5L10 2" stroke="#fff" fill="none"/></svg>info@ra-bruening-beispiel.de</p>
      <p class="contact-row"><svg viewBox="0 0 10 10"><rect x="0" y="2" width="10" height="6" fill="var(--red)"/><path d="M0 2l5 3.5L10 2" stroke="#fff" fill="none"/></svg>mandatsanfrage@ra-bruening-beispiel.de</p>
      <p class="contact-row"><svg viewBox="0 0 10 10"><rect x="0" y="2" width="10" height="6" fill="var(--red)"/><path d="M0 2l5 3.5L10 2" stroke="#fff" fill="none"/></svg>mandat@ra-bruening-beispiel.de</p>
    </section>
    <section>
      <h3>Homepage:</h3>
      <p class="contact-row"><svg viewBox="0 0 10 10"><circle cx="5" cy="5" r="4.5" fill="var(--red)"/></svg>ra-bruening-beispiel.de</p>
    </section>
    <section>
      <h3>Sprechzeiten:</h3>
      <p>Mo - Do: 09:00 - 17:00 Uhr<br>Fr: 09:00 - 16:00 Uhr<br>Sa: 09:00 - 13:00 Uhr (telefonisch)<br>weitere Termine nach<br>Vereinbarung</p>
    </section>
  </aside>

  <footer class="footer">
    <svg viewBox="0 0 680 200" preserveAspectRatio="none" aria-hidden="true">
      <path d="M0 150 C 240 120, 470 80, 680 0 L 680 200 L 0 200 Z" fill="var(--red)"/>
      <path d="M0 166 C 250 140, 480 98, 680 14 L 680 200 L 0 200 Z" fill="#fff"/>
      <path d="M0 170 C 250 146, 480 104, 680 20 L 680 200 L 0 200 Z" fill="var(--black)"/>
    </svg>
    <p class="web"><span class="dot"></span>www.ra-bruening-beispiel.de</p>
    <p class="bank">Bankinstitut: Musterbank Saar<span class="dot">•</span>IBAN: DE00 1234 5678 9012 3456 78<span class="dot">•</span>BIC: MUSTDE00</p>
  </footer>
</main>
</body>
</html>
```